Upscale business cards needed for family business

We need professional business cards created for several family members. We are a family business holding company. We would like these relatively simple and straightforward, but also with a unique element to set them apart. Probably stick with neutral and simple colors - white, grey etc. We need space for the traditional elements, including name, title, address, email/phone number. And we will be creating several from this template so it needs to be template that is easy to switch information in and out of.

Industry/Entity Type

Business

Contact Information for Business Card

Please include the attached Dunmore Ventures logo.

Requirements
Must have
• The attached Dunmore Ventures logo.

```html
<!DOCTYPE html>
<html lang="en">
<head>
<meta charset="utf-8">
<title>Dunmore Ventures – Business Card</title>
<link rel="stylesheet" href="https://fonts.googleapis.com/css2?family=Spectral:wght@400;600&family=Jost:wght@500&display=swap">
<style>
  :root {
    --page-bg: #ffffff;
    --card-bg: #ffffff;
    --card-border: #1b1b1b;
    --ink-dark: #1f2c3a;
    --ink-soft: #66777f;
    --gold-1: #e6c11c;
    --gold-2: #f4df74;
    --gold-3: #fffdf2;
    --gold-4: #e2c13c;
    --gold-5: #d7ae18;
    --spec-line: #e0389a;
    --spec-ink: #111111;
  }
  html, body {
    margin: 0;
    padding: 0;
    width: 1200px;
    height: 1176px;
    overflow: hidden;
    background: var(--page-bg);
  }
  .canvas {
    position: relative;
    width: 1200px;
    height: 1176px;
  }
  .spec-note {
    position: absolute;
    left: 470px;
    top: 100px;
    font-family: "Jost", sans-serif;
    font-weight: 500;
    font-size: 22px;
    color: var(--spec-ink);
    margin: 0;
  }
  .spec-leader {
    position: absolute;
    left: 450px;
    top: 104px;
    width: 3px;
    height: 112px;
    background: var(--spec-line);
  }
  .card {
    position: absolute;
    left: 382px;
    top: 196px;
    width: 430px;
    height: 754px;
    box-sizing: border-box;
    border: 2px solid var(--card-border);
    background: var(--card-bg);
    font-family: "Spectral", serif;
    text-align: center;
  }
  .gold-band {
    position: absolute;
    left: 2px;
    right: 2px;
    height: 29px;
    background: linear-gradient(90deg,
      var(--gold-1) 0%, var(--gold-2) 16%, var(--gold-3) 28%,
      var(--gold-4) 45%, var(--gold-1) 64%, var(--gold-3) 78%,
      var(--gold-2) 86%, var(--gold-5) 100%);
  }
  .gold-band--top { top: 1px; }
  .gold-band--bottom { bottom: 1px; }
  .brand {
    position: absolute;
    left: 0;
    right: 0;
    top: 162px;
    display: flex;
    justify-content: center;
    align-items: center;
    gap: 12px;
  }
  .brand-mark {
    width: 16px;
    height: 16px;
    border-radius: 50%;
    background: var(--ink-dark);
  }
  .brand-name {
    margin: 0;
    font-size: 30px;
    font-weight: 400;
    color: var(--ink-dark);
    line-height: 40px;
  }
  .person {
    position: absolute;
    left: 0;
    right: 0;
    top: 343px;
  }
  .person-name {
    margin: 0;
    font-size: 29px;
    font-weight: 600;
    color: var(--ink-dark);
    line-height: 38px;
  }
  .person-title {
    margin: 0;
    font-size: 21px;
    color: var(--ink-soft);
    line-height: 32px;
  }
  .contact {
    position: absolute;
    left: 0;
    right: 0;
    top: 515px;
    color: var(--ink-soft);
    font-size: 27px;
    font-style: normal;
    line-height: 37px;
  }
  .contact p { margin: 0; }
  .contact-address { margin-bottom: 19px !important; }
  .contact-phone { margin-bottom: 15px !important; }
  .contact-email { letter-spacing: 0.5px; }
</style>
</head>
<body>
<main class="canvas">
  <p class="spec-note">Metallic Gold</p>
  <div class="spec-leader"></div>

  <section class="card" aria-label="Business card front">
    <div class="gold-band gold-band--top"></div>

    <header class="brand">
      <span class="brand-mark"></span>
      <p class="brand-name">Dunmore Ventures</p>
    </header>

    <div class="person">
      <p class="person-name">EVAN MARLOWE</p>
      <p class="person-title">CONSULTANT</p>
    </div>

    <address class="contact">
      <p class="contact-address">318 Alder Crest Rd.,<br>Pasadena, CA 91105</p>
      <p class="contact-phone">818.555.0142</p>
      <p class="contact-email">Wordsmith@mailnest.com</p>
    </address>

    <div class="gold-band gold-band--bottom"></div>
  </section>
</main>
</body>
</html>
```